Business Card Design Project

Hi. We need a new business card for Brightfield Partners, a consultancy that helps people with online marketing strategy and solutions.

We have a new logo and now need the info presented - front and back of business card.

FRONT

Logo

Online strategy, consulting and coaching
Varlo Admarket consulting
Search Engine Optimisation
Internet Lead Generation
Domain name broking

BACK

Tom Bradwell-Jones
+ 61 83215 9076
+ 61 (0) 418 536 207
tom@brightfieldpartners.com.au
www.brightfieldpartners.com.au

Talkora: tombradwelljones
PO Box 312, South Perth, Western Australia 6951

Target Market(s)

Business owners, corporates

Industry/Entity Type

Marketing

Requirements
Must have
• double sided
size: 86 x 54mm
supplied as one pdf with crop marks shown (+- 1mm, with 2-3 mm bleed)

```html
<!DOCTYPE html>
<html lang="en">
<head>
<meta charset="utf-8">
<title>Brightfield Partners — Business Card</title>
<link href="https://fonts.googleapis.com/css2?family=Arimo:wght@400;700&display=swap" rel="stylesheet">
<style>
  :root {
    --page-bg: #2b2b2d;
    --blue-light: #3a80c6;
    --blue-dark: #1b4f8e;
    --brand-blue: #1f5fa8;
    --orange: #f08a1c;
    --white: #ffffff;
    --paper: #f7f7f6;
    --ink: #1a1a1a;
    --muted: #555a60;
  }
  * { box-sizing: border-box; margin: 0; padding: 0; }
  html, body {
    width: 1200px; height: 900px; overflow: hidden;
    background: var(--page-bg);
    font-family: "Arimo", Arial, sans-serif;
  }
  .canvas {
    width: 1200px; height: 900px;
    display: flex; flex-direction: column;
    align-items: center; justify-content: center; gap: 40px;
  }
  .card {
    width: 620px; height: 389px; position: relative; overflow: hidden;
    border-radius: 2px;
  }

  /* Front */
  .card--front {
    background: linear-gradient(135deg, var(--blue-light) 0%, var(--blue-dark) 100%);
    color: var(--white);
    display: flex; flex-direction: column; align-items: center; justify-content: center;
    text-align: center;
  }
  .brand {
    display: flex; align-items: center; gap: 12px;
  }
  .brand__dot {
    width: 34px; height: 34px; border-radius: 50%; background: var(--orange); flex: none;
  }
  .brand__name {
    font-weight: 700; font-size: 40px; letter-spacing: -0.5px; line-height: 1;
  }
  .card--front .brand__name { color: var(--white); }
  .front__url {
    margin-top: 10px; font-size: 12px; letter-spacing: 3px; font-weight: 700;
  }
  .front__tagline {
    margin-top: 34px; color: var(--orange); font-size: 15px;
  }
  .front__services {
    margin-top: 4px; font-size: 12.5px; line-height: 1.45;
  }

  /* Back */
  .card--back {
    background: var(--paper);
    color: var(--ink);
  }
  .card--back .brand { position: absolute; left: 34px; top: 44px; }
  .card--back .brand__dot { width: 30px; height: 30px; }
  .card--back .brand__name { color: var(--brand-blue); font-size: 33px; }
  .card--back .back__url {
    position: absolute; left: 76px; top: 86px;
    font-size: 10px; letter-spacing: 2.5px; font-weight: 700; color: var(--brand-blue);
  }
  .person {
    position: absolute; right: 34px; top: 150px; text-align: right;
  }
  .person__name { font-weight: 700; font-size: 26px; color: var(--ink); }
  .person__handle {
    margin-top: 6px; font-size: 13px; color: var(--muted);
    display: inline-flex; align-items: center; gap: 6px;
  }
  .person__handle-mark {
    width: 15px; height: 15px; border-radius: 50%; background: var(--orange);
  }
  .contacts {
    position: absolute; left: 34px; bottom: 30px; list-style: none;
    font-size: 15px; color: var(--ink); line-height: 1;
  }
  .contacts li { display: flex; align-items: center; gap: 10px; margin-top: 7px; }
  .contacts li.contacts__address { margin-top: 14px; }
  .contacts svg { width: 16px; height: 16px; flex: none; fill: var(--orange); }
</style>
</head>
<body>
<main class="canvas">

  <section class="card card--front" aria-label="Card front">
    <div class="brand">
      <span class="brand__dot"></span>
      <span class="brand__name">Brightfield Partners</span>
    </div>
    <p class="front__url">brightfieldpartners.com.au</p>
    <p class="front__tagline">Online strategy, Consulting and Coaching</p>
    <p class="front__services">
      Varlo Admarket Consulting | Search Engine Optimisation<br>
      Internet Lead Generation | Domain Name Broking
    </p>
  </section>

  <section class="card card--back" aria-label="Card back">
    <div class="brand">
      <span class="brand__dot"></span>
      <span class="brand__name">Brightfield Partners</span>
    </div>
    <p class="back__url">brightfieldpartners.com.au</p>

    <div class="person">
      <p class="person__name">Tom Bradwell-Jones</p>
      <p class="person__handle">tombradwelljones <span class="person__handle-mark" aria-label="Talkora"></span></p>
    </div>

    <ul class="contacts">
      <li>
        <svg viewBox="0 0 16 16" aria-hidden="true"><path d="M4 1h8v14H4z M5 3v9h6V3z M7.2 13h1.6v1H7.2z" fill-rule="evenodd"/></svg>
        + 61 83215 9076
      </li>
      <li>
        <svg viewBox="0 0 16 16" aria-hidden="true"><path d="M1 5c0-2 3-3 7-3s7 1 7 3v2h-3V5.5H4V7H1z M3 8h10l1 6H2z"/></svg>
        + 61 (0) 418 536 207
      </li>
      <li>
        <svg viewBox="0 0 16 16" aria-hidden="true"><path d="M1 3h14v10H1z M2.5 4.5 8 9l5.5-4.5v-0z" fill-rule="evenodd"/><path d="M1 3l7 6 7-6v1.5L8 10.5 1 4.5z" fill="#f7f7f6"/></svg>
        tom@brightfieldpartners.com.au
      </li>
      <li>
        <svg viewBox="0 0 16 16" aria-hidden="true"><path d="M8 1a7 7 0 1 0 0 14A7 7 0 0 0 8 1zm0 1.5a5.5 5.5 0 0 1 0 11 5.5 5.5 0 0 1 0-11z M7.3 2h1.4v12H7.3z M2 7.3h12v1.4H2z"/></svg>
        www.brightfieldpartners.com.au
      </li>
      <li class="contacts__address">
        <svg viewBox="0 0 16 16" aria-hidden="true"><path d="M8 1a5 5 0 0 0-5 5c0 4 5 9 5 9s5-5 5-9a5 5 0 0 0-5-5zm0 3a2 2 0 1 1 0 4 2 2 0 0 1 0-4z" fill-rule="evenodd"/></svg>
        PO Box 312, South Perth, Western Australia 6951
      </li>
    </ul>
  </section>

</main>
</body>
</html>
```